Website design for Tallow Ridge Trading Inc

We are looking to build a website for our company. We are a scrap metal recycling company based out of Los Angeles. We purchase scrap metal in the US and ship them to China for recycling into fresh metal ores to supply industrial users. We would designs that emphasize the color green given our name and the nature of our business. Recycling themes are welcomed. We already have a URL at:
http://tallowridgetradinginc.example/
At this point, I would like 4 pages:
- Home page
- About Us
- Resources
- Contact us
Our sister company is Marrow Peak Intl Inc and they have a website that we can use as a starting point.
http://www.marrowpeak-intl.example/
Our competitor has a website below. However we dislike the design given we believe it looks rather dull.
http://www.vesperalloyworks.example/en/
Lastly, this is for a website shell only. Please design the template, graphics, and color schemes. We will write the contents later.

```html
<!DOCTYPE html>
<html lang="en">
<head>
<meta charset="utf-8">
<title>Tallow Ridge Trading Inc</title>
<link href="https://fonts.googleapis.com/css2?family=Roboto:wght@300;400;700&display=swap" rel="stylesheet">
<style>
:root{
  --green:#5a9e12;
  --green-dark:#3f7a0c;
  --ink:#555;
  --ink-dark:#333;
  --bar:#3b3b3b;
  --header:#1f1f1f;
  --white:#fff;
  --orange:#f26a0c;
  --field:#eeeeee;
}
*{margin:0;padding:0;box-sizing:border-box}
html,body{width:1073px;height:1200px;overflow:hidden}
body{position:relative;font-family:'Roboto',sans-serif;font-weight:300;color:var(--ink);background:var(--white)}
.abs{position:absolute}

.news-bar{left:0;top:0;width:1073px;height:30px;background:var(--bar);color:#ddd;font-size:10.5px;line-height:30px;white-space:nowrap}
.news-bar .label{position:absolute;left:218px;color:var(--green);font-size:14px;font-weight:400}
.news-bar .stamp{position:absolute;left:316px}
.news-bar .ticker{position:absolute;left:501px}

.site-header{left:0;top:30px;width:1073px;height:83px;background:var(--header)}
.brand{position:absolute;left:196px;top:24px;display:flex;align-items:center;gap:8px}
.brand .dot{width:30px;height:30px;border-radius:50%;background:var(--green)}
.brand .name{color:var(--white);font-weight:700;font-size:22px;letter-spacing:-0.3px}
.main-nav{position:absolute;left:587px;top:33px;display:flex;color:var(--white);font-size:14px;font-weight:300}
.main-nav span{color:var(--white)}
.main-nav span.sep{margin:0 14px}

.backdrop{left:0;top:113px;width:1073px;height:1019px;
  background:linear-gradient(180deg,#5e7fab 0%,#8a7fa8 18%,#d7a08c 35%,#f2b07e 45%,#7c8fa8 58%,#2e4a7a 75%,#6a8aa6 88%,#b9c9d4 100%)}

.slider{left:173px;top:145px;width:725px;height:310px;background:var(--white);border:1px solid #ccc}
.slide{position:absolute;left:6px;top:6px;width:712px;height:298px;background:linear-gradient(180deg,#bcd6ee 0%,#d7e5ef 55%,#8c8476 70%,#6f665a 100%)}
.arrow{position:absolute;top:141px;width:28px;height:28px;border-radius:50%;background:#333c}
.arrow svg{display:block}

.panel{left:169px;top:472px;width:735px;height:632px;background:var(--white)}
.h{color:var(--green);font-weight:400}
.welcome-title{left:177px;top:486px;font-size:14.5px}
.welcome-photo{left:176px;top:523px;width:235px;height:175px;background:linear-gradient(180deg,#4f86c9 0%,#a9c4de 40%,#6a6150 65%,#3f372c 100%)}
.welcome-text{left:418px;top:519px;width:233px;font-size:9px;line-height:18.4px;text-align:justify;text-align-last:justify;color:#666}

.news-title{left:662px;top:490px;font-size:14.5px}
.news-item{width:225px}
.news-item .thumb{position:absolute;left:0;top:0;width:75px;height:57px}
.news-item .body{position:absolute;top:0;width:129px;font-size:9.6px;line-height:13.7px;color:var(--ink-dark);text-align:justify}
.news-item .body b{display:block;color:var(--green);font-weight:400}
.news-item .body .more{display:block;margin-top:3px;font-weight:400}

.card{width:230px;height:241px;background:var(--white);box-shadow:0 1px 4px rgba(0,0,0,.15)}
.card .h{position:absolute;left:19px;top:12px;font-size:14px;line-height:21.6px}
.card .pic{position:absolute;left:10px;top:62px;width:211px;height:78px}
.card .copy{position:absolute;left:19px;top:167px;width:197px;font-size:9px;line-height:18.4px;text-align:justify;color:#666}
.radios{position:absolute;left:17px;top:142px;display:flex;gap:16px;font-size:12px;color:#777}
.radios span{display:flex;align-items:center;gap:6px}
.radios i{width:8px;height:8px;border:1px solid #777;border-radius:50%;display:inline-block}
.track-btn{position:absolute;left:10px;width:211px;height:28px;color:var(--white);font-size:11.5px;font-weight:400;line-height:28px;padding-left:12px}
.track-btn svg{position:absolute;right:12px;top:6px}
.track-btn.quick{top:166px;background:linear-gradient(180deg,#555 0%,#222 100%)}
.track-btn.advanced{top:198px;background:linear-gradient(180deg,#67aa1a 0%,#2f6a0a 100%)}

.signup-text{left:169px;top:1004px;width:735px;text-align:center;font-size:10.5px;line-height:18.4px;color:#555}
.signup-field{left:316px;top:1051px;width:354px;height:27px;background:var(--field);font-size:8.5px;color:#bbb;line-height:27px;padding-left:10px}
.signup-submit{left:673px;top:1051px;width:85px;height:27px;background:var(--orange);color:var(--white);font-size:11.5px;font-weight:400;text-align:center;line-height:27px}

.site-footer{left:0;top:1132px;width:1073px;height:68px;background:var(--header);color:#ddd}
.foot-nav{position:absolute;left:171px;top:13px;font-size:10.5px;color:#ddd}
.foot-nav span{color:#ddd}
.foot-nav span.sep,.legal span.sep{margin:0 9px}
.legal{position:absolute;left:172px;top:39px;font-size:9px;color:#bbb}
.legal span{color:#bbb}
.social{position:absolute;top:26px;width:24px;height:24px;border-radius:50%}
</style>
</head>
<body>

<div class="abs news-bar">
  <span class="label">Latest News :</span>
  <span class="stamp">Last update: 23/08/2013 &nbsp;|&nbsp; 16:05</span>
  <span class="ticker">Lorem Ipsum is simply dummy text of the printing and typesetting industry.</span>
</div>

<header class="abs site-header">
  <div class="brand"><span class="dot"></span><span class="name">Tallow Ridge Trading</span></div>
  <nav class="main-nav">
    <span>Home</span><span class="sep">|</span><span>About us</span><span class="sep">|</span><span>Resources</span><span class="sep">|</span><span>Contact us</span>
  </nav>
</header>

<div class="abs backdrop" role="img" aria-label="Sunset sky over a harbour with stacked container ships"></div>

<section class="abs slider">
  <div class="slide" role="img" aria-label="Material handler crane lifting scrap metal in a recycling yard"></div>
  <span class="arrow" style="left:19px"><svg width="28" height="28" viewBox="0 0 28 28"><path d="M16 8l-6 6 6 6" fill="none" stroke="#fff" stroke-width="2.5"/></svg></span>
  <span class="arrow" style="left:674px"><svg width="28" height="28" viewBox="0 0 28 28"><path d="M12 8l6 6-6 6" fill="none" stroke="#fff" stroke-width="2.5"/></svg></span>
</section>

<main class="abs panel"></main>

<h2 class="abs h welcome-title">Welcome to Tallow Ridge Trading</h2>
<div class="abs welcome-photo" role="img" aria-label="Excavators sorting scrap in an outdoor yard under blue sky"></div>
<p class="abs welcome-text">Lorem Ipsum is simply dummy text of the printing and typesetting industry. Lorem Ipsum has been the industry's standard dummy text ever since the 1500s, when an unknown printer took a galley of type and scrambled it to make a type specimen book. It has survived not only five centuries, but also the leap into electronic typesetting, remaining essentially unchanged. It was popularised in the 1960s with the release of Pressline sheets containing Lorem Ipsum passages, and more recently with desktop publishing software like Quire Layout including</p>

<h2 class="abs h news-title">Latest News</h2>
<article class="abs news-item" style="left:667px;top:526px">
  <div class="thumb" role="img" aria-label="Demolition dust cloud over city buildings" style="background:linear-gradient(180deg,#9aa5b0,#d8d4cc 60%,#7d7468)"></div>
  <p class="body" style="left:86px;top:-2px"><b>Unde omnis iste natus</b>Contrary to popular belief, Lorem Ipsum is not simply random text. It has roots in...<span class="more">Read More</span></p>
</article>
<article class="abs news-item" style="left:662px;top:625px">
  <div class="thumb" role="img" aria-label="Excavator on a scrap heap" style="background:linear-gradient(180deg,#a9c3dc,#bfb29c 55%,#8a7a62)"></div>
  <p class="body" style="left:86px;top:-2px"><b>Unde omnis iste natus</b>Contrary to popular belief, Lorem Ipsum is not simply random text. It has roots in...<span class="more">Read More</span></p>
</article>

<section class="abs card" style="left:176px;top:730px">
  <h3 class="h">TRT Tracking</h3>
  <div class="pic" role="img" aria-label="Loaded container ship at sea" style="background:linear-gradient(180deg,#b9d3ea,#8fb0c8 45%,#3f6a86 70%,#5a8fb0)"></div>
  <div class="radios"><span><i></i>B/L</span><span><i></i>BKG</span><span><i></i>CNTR</span></div>
  <div class="track-btn quick">Quick Cargo Tracking<svg width="16" height="16" viewBox="0 0 16 16"><circle cx="8" cy="8" r="7.5" fill="#fff"/><path d="M6.5 4.5L10 8l-3.5 3.5" fill="none" stroke="#333" stroke-width="1.8"/></svg></div>
  <div class="track-btn advanced">Advanced Cargo Tracking<svg width="16" height="16" viewBox="0 0 16 16"><circle cx="8" cy="8" r="7.5" fill="#fff"/><path d="M6.5 4.5L10 8l-3.5 3.5" fill="none" stroke="#3f7a0c" stroke-width="1.8"/></svg></div>
</section>

<section class="abs card" style="left:422px;top:730px">
  <h3 class="h">Top Prices for Your Junk<br>Scrap Metals</h3>
  <div class="pic" role="img" aria-label="Yellow excavator loading scrapped cars" style="background:linear-gradient(180deg,#7fa8d0,#6c7a5a 45%,#8a6d4e 75%,#5a4a3a)"></div>
  <p class="copy">Lorem ipsum dolor sit amet, consectetur adipisicing elit, sed do eiusmod tempor incididunt ut labore et dolore magna aliqua. Lorem ipsum dolor sit amet, consectetur adipisicing elit.</p>
</section>

<section class="abs card" style="left:667px;top:730px">
  <h3 class="h">Why You Choose Us?</h3>
  <div class="pic" role="img" aria-label="Group portrait of the company team" style="background:linear-gradient(90deg,#e8e8e8,#c9a58a 40%,#b98f72 70%,#e6e6e6)"></div>
  <p class="copy">Lorem ipsum dolor sit amet, consectetur adipisicing elit, sed do eiusmod tempor incididunt ut labore et dolore magna aliqua. Lorem ipsum dolor sit amet, consectetur adipisicing elit.</p>
</section>

<p class="abs signup-text">This super awesome thing is not quite ready yet but I promise it will change your life.<br>Give me your email address and I'll hit you up when it's ready. Thanks.</p>
<div class="abs signup-field">Enter your email address...</div>
<div class="abs signup-submit">Submit</div>

<footer class="abs site-footer">
  <nav class="foot-nav"><span>Home</span><span class="sep">|</span><span>About us</span><span class="sep">|</span><span>Resources</span><span class="sep">|</span><span>Contact us</span></nav>
  <p class="legal">©2013 Company Name , All Rights Reserved<span class="sep">|</span>Privacy Policy<span class="sep">|</span>Terms &amp; Conditions</p>
  <span class="social" style="left:790px;background:#2fb5dd"></span>
  <span class="social" style="left:822px;background:#3b5998"></span>
  <span class="social" style="left:854px;background:#d9352a"></span>
  <span class="social" style="left:886px;background:#f0901e"></span>
</footer>

</body>
</html>
```